Mesa Journey Bargains Website looking for new design

We are a online travel discounter based around hotel accommodations in Las Vegas. We need a wordpress design that will be used as our corporate cover page, and also for the affiliate pages. The current design can be viewed at http://postingloom.example/clients/mesabargain/ and the final design needs to include most of the navigation components. The affiliate pages will need a space to display the booking engine, for example, as shown at http://www.qrb-voyage.example/lorenpik. Our general color scheme is red/black, and the two logos we use are attached.

Because this is a crowded niche it is extremely important that we set ourselves apart in the design. The more visually stunning and out of the box the design, the better. The site needs to look distinctively different than anything else online. Since the overall layout is very basic and does not have to provide a lot of information, it leaves a lot of flexibility in design concepts.

We realize it is a truncated timetable, which is why the increased fee for your time and guaranteed payout.

Industry/Entity Type

Travel

```html
<!DOCTYPE html>
<html lang="en">
<head>
<meta charset="utf-8">
<title>Mesa Bargains Travel</title>
<link href="https://fonts.googleapis.com/css2?family=Open+Sans:ital,wght@0,400;0,600;0,700;1,400&family=Source+Sans+3:wght@400;600&display=swap" rel="stylesheet">
<style>
:root{
  --red:#e0141b;
  --red-dark:#a80a10;
  --black:#111;
  --ink:#222;
  --grey-text:#777;
  --panel:rgba(60,60,60,.85);
  --card-bg:#efefef;
  --rule:#dcdcdc;
  --footer:#2a2a2a;
  --heading:'Source Sans 3',sans-serif;
  --body:'Open Sans',sans-serif;
}
*{box-sizing:border-box;margin:0;padding:0}
html,body{width:1200px;height:2362px;overflow:hidden;background:#fff}
body{position:relative;font-family:var(--body);color:var(--ink)}
.abs{position:absolute}
.btn{position:absolute;background:linear-gradient(#e3161d,#b00a10);color:#fff;font-family:var(--body);font-size:15px;display:flex;align-items:center;justify-content:center;border-radius:2px;box-shadow:0 2px 3px rgba(0,0,0,.25)}

/* header */
.top-line{left:0;top:0;width:1200px;height:3px;background:var(--red)}
.brand{left:60px;top:60px;display:flex;align-items:center;gap:14px}
.brand-mark{width:70px;height:70px;border-radius:50%;background:var(--red)}
.brand-name{font-family:var(--body);font-size:24px;color:var(--red);font-weight:400}
.call{left:890px;top:80px;display:flex;align-items:center;gap:14px;font-family:var(--heading);font-size:24px;color:var(--ink)}
.call-phone{left:930px;top:112px;font-family:var(--heading);font-size:38px;color:var(--red)}

/* nav */
.nav{left:0;top:186px;width:1200px;height:60px;background:linear-gradient(#ee1c22,#b70a10)}
.nav a,.footer-nav a{position:absolute;color:#fff;text-decoration:none;font-size:15px;top:20px}

/* hero */
.hero{left:0;top:246px;width:1200px;height:491px;background:linear-gradient(180deg,#5a4a48,#3a2c28)}
.hero-kicker{left:85px;top:356px;font-family:var(--heading);font-size:32px;color:#fff}
.hero-title{left:85px;top:400px;font-family:var(--heading);font-size:58px;color:#fff;letter-spacing:1px}
.hero-text{left:85px;top:482px;width:310px;font-size:13px;line-height:21px;color:#fff}
.dots{left:565px;top:698px;display:flex;gap:13px}
.dots span{width:10px;height:10px;border-radius:50%;background:#ccc}
.dots span.on{background:var(--red)}
.search{left:808px;top:246px;width:331px;height:491px;background:var(--panel);color:#fff}
.search h2{position:absolute;left:24px;top:20px;font-family:var(--heading);font-weight:400;font-size:29px}
.search label{position:absolute;font-size:15px}
.field{position:absolute;background:#fff;color:#999;font-style:italic;font-size:14px;padding:0 14px;display:flex;align-items:center}
.add-room{position:absolute;left:28px;top:376px;font-size:15px;text-decoration:underline}
.hero-shadow{left:70px;top:737px;width:1060px;height:50px;background:radial-gradient(ellipse at top,rgba(0,0,0,.3),rgba(0,0,0,0) 70%)}

/* sections */
.section-title{position:absolute;left:0;width:1200px;text-align:center;font-family:var(--heading);font-size:38px;font-weight:400;color:var(--black)}
.section-title em,.offers-title em{font-style:normal;color:var(--red)}
.welcome-text{left:64px;top:862px;width:1072px;text-align:center;font-size:13px;line-height:22px;color:var(--grey-text)}
.rule{left:60px;width:1079px;height:1px;background:var(--rule)}
.offers-title{left:60px;top:1062px;font-family:var(--heading);font-size:38px;font-weight:400;color:var(--black)}
.arrows{left:1063px;top:1065px;display:flex;gap:10px}

.card{position:absolute;top:1162px;width:334px;height:566px;background:var(--card-bg)}
.card-photo{height:241px;background:linear-gradient(180deg,#7fa9c4,#4f8a90)}
.card-photo.canal{background:linear-gradient(180deg,#3a4c72,#2c3448)}
.card-photo.boat{background:linear-gradient(180deg,#8fb0b8,#4f9aa4)}
.card-band{height:60px;display:flex;justify-content:space-between;align-items:center;padding:0 18px;color:#fff;font-family:var(--heading);font-size:24px;background:linear-gradient(#f01c22,#b80a10)}
.card-band.dark{height:58px;background:linear-gradient(#3a3a3a,#050505)}
.card p{padding:18px 17px 0;font-size:13px;line-height:22px;color:#333}
.card .btn{left:16px;top:492px;width:115px;height:45px}

/* contact */
.input{position:absolute;border:1px solid #cfcfcf;background:#fff;color:#888;font-style:italic;font-size:14px;padding:0 16px;display:flex;align-items:center}
.info{left:687px;font-size:16px;color:var(--ink);display:flex;align-items:center;gap:16px}
.social{top:2032px;width:46px;height:46px;border:1.5px solid #bbb;border-radius:50%}

/* footer */
.footer{left:0;top:2252px;width:1200px;height:110px;background:var(--footer)}
.footer-nav a{color:#8c8c8c;top:38px;font-size:15px}
.copyright{position:absolute;left:0;top:64px;width:1200px;text-align:center;font-size:12.5px;color:#666}
</style>
</head>
<body>

<div class="abs top-line"></div>
<header>
  <div class="abs brand"><span class="brand-mark"></span><span class="brand-name">mesabargains.travel</span></div>
  <div class="abs call">
    <svg width="24" height="24" viewBox="0 0 24 24"><rect width="24" height="24" rx="4" fill="#e0141b"/><path d="M8 5.5l2.2 3-1.4 1.6a8 8 0 0 0 5 5l1.6-1.4 3 2.2-1.3 2.4c-5.6.2-11.4-5.6-11.2-11.2z" fill="#fff"/></svg>
    Call us Now :
  </div>
  <div class="abs call-phone">555-014-2290</div>
</header>

<nav class="abs nav">
  <a style="left:60px">HOME</a>
  <a style="left:150px">GROUPS</a>
  <a style="left:257px">SEARCH EVENTS</a>
  <a style="left:417px">CONTACT US</a>
</nav>

<section>
  <div class="abs hero" role="img" aria-label="Resort terrace at sunset with palm tree, parasols and sea view"></div>
  <div class="abs hero-kicker">TRAVEL .</div>
  <div class="abs hero-title">DISCOUNTER</div>
  <p class="abs hero-text">We provide hotel accommodations at wholesale prices, for any size group, large or small.</p>
  <div class="btn" style="left:85px;top:543px;width:115px;height:46px">READ MORE</div>
  <div class="abs dots"><span></span><span class="on"></span><span></span></div>

  <form class="abs search">
    <h2>Hotel Search</h2>
    <label style="left:28px;top:76px">Location</label>
    <div class="field" style="left:28px;top:108px;width:271px;height:46px">Please Typre Your City name</div>
    <label style="left:28px;top:174px">Check In</label>
    <label style="left:170px;top:174px">Check Out</label>
    <div class="field" style="left:28px;top:209px;width:129px;height:46px">Date</div>
    <div class="field" style="left:170px;top:209px;width:129px;height:46px">Date</div>
    <label style="left:28px;top:273px">Rooms</label>
    <label style="left:120px;top:273px">Childrens</label>
    <div class="field" style="left:28px;top:308px;width:70px;height:46px"></div>
    <div class="field" style="left:120px;top:308px;width:69px;height:46px"></div>
    <span class="add-room">Add another room +</span>
    <div class="btn" style="left:24px;top:417px;width:88px;height:44px;font-weight:700;font-size:14px">SEARCH</div>
  </form>
  <div class="abs hero-shadow"></div>
</section>

<section>
  <h1 class="section-title" style="top:798px">WELCOME TO <em>MESABARGAINS</em></h1>
  <p class="abs welcome-text">Nemo enim ipsam voluptatem quia voluptas sit aspernatur aut odit aut fugit, sed quia consequuntur magni dolores eos qui ratione voluptatem sequi nesciunt. Neque porro quisquam est, qui dolorem ipsum quia dolor sit amet, consectetur, adipisci velit, sed quia non numquam eius modi tempora incidunt ut labore et dolore magnam aliquam quaerat voluptatem. Ut enim ad minima veniam, quis nostrum exercitationem ullam corporis suscipit laboriosam</p>
  <div class="btn" style="left:543px;top:953px;width:114px;height:46px">READ MORE</div>
</section>

<div class="abs rule" style="top:1027px"></div>

<section>
  <h2 class="abs offers-title">POPULAR <em>OFFERS</em></h2>
  <div class="abs arrows">
    <svg width="33" height="33" viewBox="0 0 33 33"><circle cx="16.5" cy="16.5" r="14.5" fill="none" stroke="#111" stroke-width="3"/><path d="M24 16.5H11M16 11l-5.5 5.5L16 22" fill="none" stroke="#111" stroke-width="3"/></svg>
    <svg width="33" height="33" viewBox="0 0 33 33"><circle cx="16.5" cy="16.5" r="14.5" fill="none" stroke="#111" stroke-width="3"/><path d="M9 16.5h13M17 11l5.5 5.5L17 22" fill="none" stroke="#111" stroke-width="3"/></svg>
  </div>

  <article class="card" style="left:60px">
    <div class="card-photo" role="img" aria-label="Tropical bay with limestone cliffs and longtail boats"></div>
    <div class="card-band"><span>Exotic Tahiti</span><span>12 Days</span></div>
    <div class="card-band dark"><span>Special Offer</span><span>$1299</span></div>
    <p>In pellentesque faucibus vestibulum. Nulla at nulla justo, eget luctus tortor. Nulla facilisi. Duis aliquet egestas purus in blandit. Curabitur vulputate, ligula lacinia scelerisque tempor.</p>
    <div class="btn">BOOK NOW</div>
  </article>
  <article class="card" style="left:433px">
    <div class="card-photo canal" role="img" aria-label="City canal at dusk lined with lit buildings"></div>
    <div class="card-band"><span>Exotic Tahiti</span><span>12 Days</span></div>
    <div class="card-band dark"><span>Special Offer</span><span>$1299</span></div>
    <p>In pellentesque faucibus vestibulum. Nulla at nulla justo, eget luctus tortor. Nulla facilisi. Duis aliquet egestas purus in blandit. Curabitur vulputate, ligula lacinia scelerisque tempor.</p>
    <div class="btn">BOOK NOW</div>
  </article>
  <article class="card" style="left:802px">
    <div class="card-photo boat" role="img" aria-label="Wooden boat on turquoise water beside cliffs"></div>
    <div class="card-band"><span>Exotic Tahiti</span><span>12 Days</span></div>
    <div class="card-band dark"><span>Special Offer</span><span>$1299</span></div>
    <p>In pellentesque faucibus vestibulum. Nulla at nulla justo, eget luctus tortor. Nulla facilisi. Duis aliquet egestas purus in blandit. Curabitur vulputate, ligula lacinia scelerisque tempor.</p>
    <div class="btn">BOOK NOW</div>
  </article>
</section>

<div class="abs rule" style="top:1766px"></div>

<section>
  <h2 class="section-title" style="top:1792px">CONTACT US <em>TODAY</em></h2>
  <div class="input" style="left:60px;top:1885px;width:291px;height:58px">First&nbsp; Name</div>
  <div class="input" style="left:359px;top:1885px;width:291px;height:58px">Last Name</div>
  <div class="input" style="left:60px;top:1951px;width:291px;height:59px">Enter Your Mail Id</div>
  <div class="input" style="left:359px;top:1951px;width:291px;height:59px">Enter Your Phone Number</div>
  <div class="input" style="left:60px;top:2021px;width:590px;height:138px;align-items:flex-start;padding-top:16px">Enter Your Message</div>
  <div class="btn" style="left:60px;top:2173px;width:91px;height:46px;font-weight:700;font-size:14px">SUBMIT</div>

  <div class="abs info" style="top:1879px">Name: Dana K. Whitfield</div>
  <div class="abs info" style="top:1926px">
    <svg width="18" height="18" viewBox="0 0 18 18"><rect width="18" height="18" rx="3" fill="#222"/><path d="M4 6h10v7H4zM4 6l5 4 5-4" fill="none" stroke="#fff" stroke-width="1.3"/></svg>
    <span style="text-decoration:underline">Email: DanaKWhitfield@mailbox.example</span>
  </div>
  <div class="abs info" style="top:1970px">
    <svg width="18" height="18" viewBox="0 0 24 24"><rect width="24" height="24" rx="4" fill="#222"/><path d="M8 5.5l2.2 3-1.4 1.6a8 8 0 0 0 5 5l1.6-1.4 3 2.2-1.3 2.4c-5.6.2-11.4-5.6-11.2-11.2z" fill="#fff"/></svg>
    Phone: 555-014-2290
  </div>
  <div class="abs social" style="left:683px"></div>
  <div class="abs social" style="left:746px"></div>
  <div class="abs social" style="left:809px"></div>
</section>

<footer class="abs footer">
  <nav class="footer-nav">
    <a style="left:374px">HOME</a>
    <a style="left:465px">GROUPS</a>
    <a style="left:572px">SEARCH EVENTS</a>
    <a style="left:733px">CONTACT US</a>
  </nav>
  <p class="copyright">Copyright © 2015 MesaBargains.Travel. All Rights Reserved.</p>
</footer>

</body>
</html>
```